Website for a company offering full serivce charging solutions for electric cars

The company "vorn-werk" (english: "front-works") offering all-in-one-solutions for charging infrastructure for electric mobility.

There are four products:
1- Wallboxes for single-family homes
2- Solutions for property devloper/-management for property parking space
3- All-in-one-charging solution for municipalities/communities
4- Solutions for tourism/hotels/holiday appartments

The Website structure:
1. Main Page
2.1. Product Page Single Homes
2.2. Product Page Property Management / Parking
2.3. Product Page Municipality
2.4. Product Page Tourism
3. Contact Form / Request for information
4. Imprint / Legal

The Website should be built on Wordpress with a powerful possibility to simply add/modify specific landing pages.

We would like you to implement the website later and also maintain it if possible, but we would be able to do minor modifications by ourselfs (for A/B-Testing)

The website should be clear and simple, easy to understand.
Target group is mainly B2C without deeper knowledge of that topic.

It should suggest, that we will provide a very simple way to get the charging infrastructure done.

We need a contact form, maybe we will use Leadmill later.

Attached you will find a draft of the main page and a landing page (for 2.2) - it is just the content, please ignore the design. We would love to let you create a suitable design.
Also you will find some drafts a bit different for the same story.

I added also a few stock photos, but they don't need to be used! If you have better ideas, you are welcome!

Charging/Electric mobility

Sans Serif

• Based on Wordpress, and the designer should be able to implement it on Wordpress on a later step

```html
<!DOCTYPE html>
<html lang="de">
<head>
<meta charset="utf-8">
<title>vorn-werk – einfach mehr als laden</title>
<link href="https://fonts.googleapis.com/css2?family=Poppins:wght@400;500;600&family=Righteous&display=swap" rel="stylesheet">
<style>
:root{
  --bg:#131a29;
  --header:#141a2b;
  --magenta:#d42ba3;
  --purple:#7a4bc4;
  --white:#ffffff;
  --text:#e9e9f0;
  --muted:#cfd0da;
}
*{box-sizing:border-box;margin:0;padding:0}
html,body{width:1200px;height:2877px;overflow:hidden;background:var(--bg);font-family:"Poppins",sans-serif;color:var(--text)}
.page{position:relative;width:1200px;height:2877px}

/* header */
.site-header{position:absolute;left:0;top:0;width:1200px;height:88px;background:var(--header);border-bottom:2px solid var(--magenta)}
.brand{position:absolute;left:104px;top:22px;display:flex;align-items:center;gap:12px}
.brand-mark{width:26px;height:26px;border-radius:50%;background:var(--magenta)}
.brand-name{font-size:27px;font-weight:500;color:var(--white);line-height:1}
.brand-tag{display:block;font-size:13px;font-weight:400;color:var(--white);margin-top:4px;padding-left:14px}
.main-nav{position:absolute;top:33px;left:546px;display:flex;gap:44px;font-size:17px;font-weight:500;color:var(--white)}
.main-nav .active{color:var(--magenta)}

/* hero */
.hero{position:absolute;left:0;top:88px;width:1200px;height:645px;
  background:radial-gradient(circle at 22% 20%,rgba(200,190,255,.35),transparent 30%),
  linear-gradient(100deg,#3c3f80 0%,#5a4f9a 30%,#2a2f55 55%,#1c2140 70%,#1b3a9e 100%)}
.hero-title{position:absolute;left:100px;top:210px;font-family:"Righteous",sans-serif;font-size:68px;color:var(--white);letter-spacing:1px}
.hero-sub{position:absolute;left:100px;top:298px;font-size:40px;font-weight:400;color:var(--white)}
.hero-btn{position:absolute;left:102px;top:370px;width:153px;height:43px;border-radius:22px;
  background:linear-gradient(90deg,#9b3bd0,#d42ba3);color:var(--white);font-size:15px;font-weight:600;display:flex;align-items:center;justify-content:center}
.hero-arrow{position:absolute;top:300px}
.hero-dots{position:absolute;top:594px;left:560px;display:flex;gap:11px}
.hero-dots span{width:12px;height:12px;border-radius:50%;border:1.5px solid var(--white)}
.hero-dots .on{background:var(--white)}

/* partner */
.partner-frame{position:absolute;left:84px;top:820px;width:470px;height:526px;border-radius:22px;background:linear-gradient(180deg,var(--purple),var(--magenta))}
.partner-photo{position:absolute;left:98px;top:832px;width:468px;height:514px;border-radius:20px;
  background:linear-gradient(160deg,#e8a24a 0%,#c8893e 30%,#4a3b34 60%,#cfd3d8 100%)}
.partner-text{position:absolute;left:647px;top:845px;width:460px}
.partner-text h2{font-family:"Righteous",sans-serif;font-size:37px;color:var(--magenta);font-weight:400;margin-left:-1px;margin-bottom:18px}
.lead{font-size:15.5px;line-height:29px;color:var(--white);margin-bottom:10px}
.partner-text p.body{font-size:13.2px;line-height:29.5px;color:var(--white);margin-bottom:8px}
.hl{color:var(--magenta)}

/* offers */
.offer{position:absolute;top:1434px;width:326px;height:1126px;border:2px solid var(--magenta)}
.offer-photo{height:216px;background:linear-gradient(135deg,#dfe6f2,#5a7bd8 55%,#1d2fb0)}
.offer h3{font-family:"Righteous",sans-serif;font-weight:400;font-size:27px;color:var(--magenta);margin:18px 0 0 31px}
.offer ul{list-style:none;margin:22px 8px 0 22px}
.offer li{position:relative;padding-left:17px;font-size:14.6px;line-height:20.5px;color:var(--text);margin-bottom:18px}
.offer li::before{content:"";position:absolute;left:0;top:6px;width:9px;height:9px;border-radius:50%;border:2px solid var(--magenta);box-shadow:inset 0 0 0 1.5px var(--bg);background:var(--magenta)}
.offer li.tight{margin-bottom:10px}
.offer ul.sub{margin:16px 0 0 0}
.offer ul.sub li{font-size:12px;line-height:16px;margin-bottom:7.5px;padding-left:15px;white-space:nowrap}
.offer ul.sub li::before{content:"-";border:0;box-shadow:none;background:none;color:var(--magenta);top:-1px;width:auto;height:auto}

/* footer */
.footer-line{position:absolute;left:0;top:2662px;width:1200px;height:4px;background:linear-gradient(90deg,var(--purple),var(--magenta))}
.social{position:absolute;top:2718px;left:513px;display:flex;gap:15px}
.social span{width:48px;height:48px;border-radius:50%;background:linear-gradient(135deg,#9b3bd0,#d42ba3)}
.footer-links{position:absolute;top:2788px;left:0;width:1200px;display:flex;justify-content:center;gap:30px;font-size:16px;color:var(--white)}
.copyright{position:absolute;top:2832px;width:1200px;text-align:center;font-size:16px;color:var(--white)}
</style>
</head>
<body>
<div class="page">

<header class="site-header">
  <div class="brand">
    <span class="brand-mark"></span>
    <div><span class="brand-name">vorn-werk.de</span><span class="brand-tag">einfach mehr als laden</span></div>
  </div>
  <nav class="main-nav">
    <span class="active">Lösungen</span><span>Unternehmen</span><span>Services</span><span>Karriere</span><span>Kontakt</span>
  </nav>
</header>

<section class="hero" role="img" aria-label="Ladestecker an einer Ladesäule vor unscharfen Parkplatzlichtern">
  <div class="hero-title">vorn werk de</div>
  <div class="hero-sub">einfach mehr als laden</div>
  <div class="hero-btn">GET STARTED</div>
  <svg class="hero-arrow" style="left:56px" width="26" height="44" viewBox="0 0 26 44"><path d="M23 2 3 22l20 20" fill="none" stroke="#fff" stroke-width="2.5"/></svg>
  <svg class="hero-arrow" style="left:1112px" width="26" height="44" viewBox="0 0 26 44"><path d="M3 2l20 20L3 42" fill="none" stroke="#fff" stroke-width="2.5"/></svg>
  <div class="hero-dots"><span></span><span></span><span class="on"></span><span></span></div>
</section>

<div class="partner-frame"></div>
<div class="partner-photo" role="img" aria-label="Frau mit Smartphone lädt ihr Elektroauto bei Sonnenuntergang"></div>
<section class="partner-text">
  <h2>vorn-werk ist Ihr Partner</h2>
  <p class="lead">wenn das Laden nicht nur einfach, sondern die Umsetzung auch aus einer Hand kommen soll</p>
  <p class="body">Wir&nbsp; bieten Lösungen sowohl für <span class="hl">Privatkunden, Geschäftskunden</span> als auch <span class="hl">Kommunen</span> an, die schnell, fair und ohne Eigenleistung zu einer smarten Ladelösung für E-Fahrzeuge kommen möchten.</p>
  <p class="body">Von der Beratung, über die Installation, Inbetriebnahme bis zur Abrechnung und Wartung bekommen Sie bei vorn-werk alles aus einer Hand. Auf Wunsch vermieten wir auch die Ladetechnik und übernehmen im gewerblichen Bereich die direkte Abrechnung mit dem Nutzer. Für Kommunen bieten wir den kostenfreien Full-Service an und beteiligen die Gemeinden an der Nutzung der Infrastruktur.</p>
  <p class="body">Fragen Sie uns nach der auf Ihre individuellen Bedürfnisse zugeschnittenen Lösung:</p>
</section>

<article class="offer" style="left:97px">
  <div class="offer-photo" role="img" aria-label="Ladestecker in beleuchteter Wallbox"></div>
  <h3>als Privatkunde</h3>
  <ul>
    <li>Bestandsanalyse mit umfangre&shy;icher Beratung über die Möglich&shy;keiten der Umsetzung</li>
    <li>Prüfung und Übernahme der An&shy;meldung verfügbarer Förder&shy;möglichkeiten</li>
    <li>Auswahl an smarten Wallbox Lösungen, passend für Ihr Fahrze&shy;ug und Ihre Bedürfnisse</li>
    <li>Installation inkl. aller notwendigen Materialien und Tätigkeiten (Durchbrüche, Erdarbeiten, etc.</li>
    <li>Inbetriebnahme und Einweisung in die Ladetechnik</li>
    <li>Jährlich technische Wartung nach DGUV3</li>
    <li>Reparaturservice, unter Berück&shy;sichtigung der geltenden Garantie Ansprüche</li>
  </ul>
</article>

<article class="offer" style="left:436px">
  <div class="offer-photo" role="img" aria-label="Ladekabel steckt am Elektroauto"></div>
  <h3>als Geschäftskunde</h3>
  <ul>
    <li>Durchführung einer individuellen Bedarfsanalyse inkl. Ermittlung der Anforderungen für:
      <ul class="sub">
        <li>Haus- und Immobilienverwaltungen</li>
        <li>Dienstleistungs- und Handelsunternehmen</li>
        <li>Hotel und Beherbergungsbetriebe</li>
        <li>Parkraum- und Parkhausbetreiber</li>
        <li>Tourismus, Sport- und Freizeiteinrichtungen</li>
      </ul>
    </li>
    <li>Planung und Projektierung des Installationsaufwands inkl. Materialverbrauch</li>
    <li class="tight">Leasing oder Kauf der Hardware</li>
    <li>Normgerechte Installation der Ladeinfrastruktur inkl. Durch&shy;bruch-, Brandschutz- und Erdar&shy;beiten</li>
    <li>Bei Bestandsbauten Integration der Ladeinfrastruktur in die Geb&shy;äudesystemtechnik und ggf. An&shy;passung des Netzanschlusses</li>
    <li class="tight">Inbetriebnahme der Anlage inkl. Prüf- und Messprotokollen</li>
    <li class="tight">Wiederkehrende technische Prü&shy;fung der Anlage nach DGUV 3</li>
    <li class="tight">Austausch und Reparatur Service</li>
    <li class="tight">Unterstützung bei der mtl. Nutzu&shy;ngsabrechnung und Einbindung in Ihre vorhandene Abrech&shy;nungssysteme</li>
    <li>ODER direkte Abrechnung mit den Nutzern</li>
  </ul>
</article>

<article class="offer" style="left:775px">
  <div class="offer-photo" role="img" aria-label="Elektroauto an Ladesäule mit Lichteffekten"></div>
  <h3>als Kommune</h3>
  <ul>
    <li>Konzeptionierung möglicher Ladeinfrastrukturen innerhalb Ihrer Gemeinde</li>
    <li>Planung und Projektsteuerung inkl. sämtlicher behördlicher Genehmigungsverfahren und Beantragung von Fördermitteln</li>
    <li>Fachgerechte Installation und I nbetriebnahme</li>
    <li class="tight">Regelmäßige Wartung gemäß Vorschrif</li>
    <li class="tight">Reparatur und Kundenservice</li>
    <li>Direkte Abrechnung mit dem Nutzer</li>
    <li>Beteiligung der Gemeinde am Umsatz</li>
    <li>Möglichkeit der Integration von Bonusprogrammen, mit denen der lokale Einzelhandel beworben wird</li>
  </ul>
</article>

<footer>
  <div class="footer-line"></div>
  <div class="social"><span></span><span></span><span></span></div>
  <div class="footer-links">
    <span>AGB Datenschutzerklarung</span><span>|</span><span>Impressum</span><span>|</span><span>Kontakt</span><span>|</span><span>Karriere</span><span>|</span><span>FAQ</span>
  </div>
  <div class="copyright">©vorn-werk GmbH</div>
</footer>

</div>
</body>
</html>
```